81M business card

I need a business card for a life sciences consulting firm I started. The company name is 81M and the logo is attached. I am looking for something edgey and current but different from the blah standard business card.

Industry/Entity Type

Business

Requirements
Nice to have
• Both sides

```html
<!DOCTYPE html>
<html lang="en">
<head>
<meta charset="utf-8">
<title>81M Business Card</title>
<link rel="stylesheet" href="https://fonts.googleapis.com/css2?family=Ubuntu:wght@400;500;700&display=swap">
<style>
  :root {
    --navy: #1d3a8a;
    --orange: #ec7a1c;
    --card: #f4f4f5;
    --card-shade: #e4e4e6;
    --ghost: #e2e3e8;
    --backdrop: #e9e7e4;
    --muted: #6b6f7b;
  }
  * { box-sizing: border-box; margin: 0; padding: 0; }
  html, body {
    width: 1200px; height: 900px; overflow: hidden;
    background: var(--backdrop);
    font-family: "Ubuntu", sans-serif;
  }
  .stage { position: relative; width: 1200px; height: 900px; }
  .card {
    position: absolute; width: 520px; height: 297px;
    border-radius: 22px; overflow: hidden;
    background: linear-gradient(160deg, #ffffff 0%, var(--card) 55%, var(--card-shade) 100%);
    box-shadow: 0 14px 30px rgba(0,0,0,.18);
  }
  .card--front { left: 90px; top: 90px; }
  .card--back { left: 590px; top: 510px; }

  /* Brand lockup */
  .brand { position: absolute; display: flex; align-items: center; gap: 10px; }
  .brand__square { width: 14px; height: 14px; background: var(--orange); flex: none; }
  .brand__text { display: flex; flex-direction: column; }
  .brand__name { font-weight: 500; font-size: 28px; color: var(--navy); line-height: 1; }
  .brand__tagline { font-weight: 500; font-size: 7px; color: var(--muted); margin-top: 4px; }

  .card--front .brand { left: 32px; bottom: 38px; }
  .card--back .brand { right: 36px; top: 118px; }

  /* Large name on front */
  .hero-name {
    position: absolute; right: 44px; top: 60px;
    font-weight: 500; font-size: 120px; line-height: 1;
    color: var(--navy);
  }

  /* Faint large name on back */
  .ghost-name {
    position: absolute; left: 30px; top: 20px;
    font-weight: 500; font-size: 150px; line-height: 1;
    color: var(--ghost);
  }

  .person { position: absolute; left: 36px; top: 118px; }
  .person__name { font-weight: 700; font-size: 17px; color: var(--navy); }
  .person__role { font-size: 11px; color: var(--orange); font-weight: 500; margin-top: 1px; }

  .contact { position: absolute; left: 150px; top: 162px; list-style: none; }
  .contact__item {
    display: flex; align-items: center; gap: 12px;
    font-size: 13px; font-weight: 500; color: var(--navy); margin-bottom: 10px;
  }
  .contact__icon { width: 12px; height: 14px; color: var(--orange); flex: none; }
</style>
</head>
<body>
<main class="stage">

  <section class="card card--front" aria-label="Card front">
    <p class="hero-name">81M</p>
    <div class="brand">
      <div class="brand__square"></div>
      <div class="brand__text">
        <span class="brand__name">81M</span>
        <span class="brand__tagline">life sciences strategy partners</span>
      </div>
    </div>
  </section>

  <section class="card card--back" aria-label="Card back">
    <p class="ghost-name" aria-hidden="true">81M</p>
    <div class="person">
      <p class="person__name">Daniel Reyes</p>
      <p class="person__role">general manager</p>
    </div>
    <ul class="contact">
      <li class="contact__item">
        <svg class="contact__icon" viewBox="0 0 12 14" aria-hidden="true">
          <rect x="2.5" y="0.8" width="7" height="12.4" rx="1.3" fill="none" stroke="currentColor" stroke-width="1.4"/>
          <circle cx="6" cy="10.8" r="0.9" fill="currentColor"/>
        </svg>
        0400 555 018
      </li>
      <li class="contact__item">
        <svg class="contact__icon" viewBox="0 0 14 14" aria-hidden="true">
          <text x="0" y="12" font-family="Ubuntu, sans-serif" font-size="13" font-weight="700" fill="currentColor">@</text>
        </svg>
        dreyes@81m.com
      </li>
    </ul>
    <div class="brand">
      <div class="brand__square"></div>
      <div class="brand__text">
        <span class="brand__name">81M</span>
        <span class="brand__tagline">life sciences strategy partners</span>
      </div>
    </div>
  </section>

</main>
</body>
</html>
```